Palisade Lift Inc Website Deisgn

We are a new small elevator contracting company.
We would like a full website designed similar to
http://brightmorelift.com or https://www.northpeaklifting.ca/
In addition to contents found on the above webpages.. we would like a section for project gallery etc.... have fun with it ... make it professional

Target Market(s)

Elevator Consultants - Property managers - Condo Boards - Commercial office buildings

Coding

Coded - Design and coding required

Number of Pages Required

5+ page

Requirements
Must have
• Navigation Bar.. Be view able via mobile ..Should be pictures of Tall Office buildings in background.. Toronto city skyline etc....

Have Fun!

```html
<!DOCTYPE html>
<html lang="en">
<head>
<meta charset="utf-8">
<title>Palisade Lift Inc</title>
<link href="https://fonts.googleapis.com/css2?family=Rajdhani:wght@500;600;700&family=Roboto:wght@400;500;700&display=swap" rel="stylesheet">
<style>
:root{
  --blue:#10a4f9;
  --navy:#0b1f3f;
  --navy-deep:#081833;
  --ink:#1b1b1b;
  --muted:#6f7680;
  --light:#f4f5f7;
  --white:#ffffff;
}
*{box-sizing:border-box;margin:0;padding:0}
html,body{width:1200px;height:4501px;overflow:hidden}
body{position:relative;font-family:'Roboto',sans-serif;color:var(--ink);background:var(--white)}
.abs{position:absolute}
.head{font-family:'Rajdhani',sans-serif;font-weight:700}
.label{font-family:'Roboto',sans-serif;font-weight:700;font-size:11px;letter-spacing:.5px;text-transform:uppercase;color:var(--blue)}
.title{font-family:'Rajdhani',sans-serif;font-weight:700;font-size:32px;line-height:1.1}
.underline{height:2px;width:84px;background:var(--blue)}
.body-text{font-size:11px;line-height:19px;color:var(--muted)}
.more{font-size:12px;font-weight:700;color:var(--blue);letter-spacing:.3px;display:flex;align-items:center;gap:6px}
.more svg{width:16px;height:10px}

/* hero */
.hero{left:0;top:0;width:1200px;height:713px;background:linear-gradient(180deg,#2e3a52 0%,#3d4a62 40%,#253249 75%,#1a2438 100%)}
.brand{color:var(--white);font-family:'Rajdhani',sans-serif;font-weight:700;font-size:32px;line-height:1;letter-spacing:.5px}
.nav{left:511px;top:35px;display:flex;gap:20px;font-size:12px;color:var(--white)}
.quote-btn{left:926px;top:25px;width:113px;height:40px;background:var(--blue);color:var(--white);font-size:13px;font-weight:700;display:flex;align-items:center;justify-content:center}
.hero-rule{left:161px;top:88px;width:878px;height:1px;background:rgba(255,255,255,.2)}
.hero-title{left:0;top:232px;width:1200px;text-align:center;color:var(--white);font-size:50px;line-height:60px;letter-spacing:.5px}
.hero-title span{color:var(--blue)}
.hero-sub{left:300px;top:354px;width:600px;text-align:center;color:#e4e8ef;font-size:12.5px;line-height:23px}
.hero-btn{left:489px;top:447px;width:222px;height:54px;background:var(--blue);color:var(--white);font-size:15px;font-weight:700;display:flex;align-items:center;justify-content:center}

/* about */
.about-band{left:0;top:713px;width:599px;height:335px;background:var(--blue)}
.about-img{left:213px;top:877px;width:713px;height:337px;background:linear-gradient(90deg,#4a4e55,#7a7f86 35%,#5a5e64 60%,#8a8e94)}
.about-card{left:611px;top:1099px;width:427px;height:260px;background:var(--white);box-shadow:0 8px 28px rgba(0,0,0,.08);padding:42px 34px}

/* dark section */
.dark{left:0;top:1450px;width:1200px;height:788px;background:var(--navy)}
.gallery-img{top:1630px;width:240px;height:299px}
.col-rule{top:1630px;width:1px;height:335px;background:rgba(255,255,255,.12)}
.services{left:180px;top:2116px;width:838px;height:260px;display:flex}
.service{width:210px;height:260px;background:var(--light);padding:26px 20px}
.service.active{background:var(--blue)}
.service .icon{width:44px;height:44px;margin-bottom:22px}
.service h3{font-size:12.5px;font-weight:700;color:var(--ink);margin-bottom:4px}
.service .bar{width:50px;height:1px;background:var(--blue);margin-bottom:10px}
.service p{font-size:10.5px;line-height:19px;color:var(--muted);margin-bottom:14px}
.service.active h3,.service.active p,.service.active .more{color:var(--white)}
.service.active .bar{background:var(--white)}

/* video */
.video{left:239px;top:2482px;width:713px;height:336px;background:linear-gradient(180deg,#4a5666 0%,#2f3b4b 55%,#1d2632 100%)}
.play{left:566px;top:2620px;width:68px;height:68px;border-radius:50%;background:var(--blue);box-shadow:0 0 0 8px rgba(16,164,249,.3);display:flex;align-items:center;justify-content:center}

/* faq */
.faq-img{left:0;top:2940px;width:563px;height:449px;background:linear-gradient(90deg,#3a3330,#6b5a4c 30%,#4a4440 60%,#2d2926)}
.faq-card{left:484px;top:3087px;width:501px;height:224px;background:var(--white);box-shadow:0 8px 28px rgba(0,0,0,.08);padding:34px 31px}
.faq-card h4{font-size:13px;font-weight:700;line-height:19px;margin-bottom:10px}
.faq-card h4 span{color:var(--blue)}
.dots{left:596px;top:3347px;display:flex;gap:8px}
.dots i{display:block;width:22px;height:2px;background:#d8dbe0}
.dots i.on{background:var(--blue)}

/* contact */
.contact{left:0;top:3389px;width:1200px;height:751px;background:var(--light)}
.contact-info{left:199px;top:3634px;width:351px;height:332px;background:var(--white);padding:60px 34px}
.info-item{margin-bottom:40px}
.info-item .h{display:flex;align-items:center;gap:10px;color:var(--blue);font-family:'Rajdhani',sans-serif;font-weight:700;font-size:19px}
.info-item .h svg{width:18px;height:18px}
.info-item p{font-size:11px;color:var(--muted);margin-top:6px}
.contact-btn{left:199px;top:3987px;width:351px;height:57px;background:var(--navy);color:var(--white);font-size:15px;font-weight:700;display:flex;align-items:center;justify-content:center}
.contact-form{left:573px;top:3634px;width:428px;height:410px;background:var(--white);padding:36px 37px}
.field{border-bottom:1px solid #d9dce1;font-size:10px;color:var(--muted);padding-bottom:12px;margin-bottom:40px}
.field.msg{padding-bottom:52px;margin-bottom:40px}
.send{width:195px;height:57px;background:var(--blue);color:var(--white);font-size:15px;font-weight:700;display:flex;align-items:center;justify-content:center}

/* footer */
.footer{left:0;top:4140px;width:1200px;height:361px;background:linear-gradient(180deg,#1f2c45,#162238 60%,var(--navy-deep))}
.foot-nav{left:0;top:4284px;width:1200px;display:flex;justify-content:center;gap:20px;font-size:12px;color:var(--white)}
.foot-rule{left:161px;top:4330px;width:878px;height:1px;background:rgba(255,255,255,.15)}
.follow{left:0;top:4345px;width:1200px;text-align:center;font-size:12px;font-weight:700;color:var(--white)}
.social{left:513px;top:4376px;display:flex;gap:8px}
.social i{display:block;width:37px;height:37px;border:1px solid rgba(255,255,255,.6)}
.social i.on{background:var(--blue);border-color:var(--blue)}
.copy{left:0;top:4469px;width:1200px;text-align:center;font-size:10.5px;color:#cdd3dc}
.copy span{color:var(--blue)}
</style>
</head>
<body>

<!-- Hero -->
<div class="abs hero" role="img" aria-label="Dusk photo of a downtown city skyline with tall office towers and traffic"></div>
<div class="abs brand" style="left:161px;top:28px">PALISADE LIFT INC</div>
<nav class="abs nav"><span>Home</span><span>About Us</span><span>Services</span><span>Gallery</span><span>Faq</span><span>Contact Us</span></nav>
<div class="abs quote-btn">Free Quote</div>
<div class="abs hero-rule"></div>
<h1 class="abs head hero-title">NEXT LEVEL SERVICE AND MAINTANENCE<br>FOR <span>THE ELEVATOR</span> INDUSTRY</h1>
<p class="abs hero-sub">Lorem Ipsum is simply dummy text of the printing and typesetting industry. Lorem Ipsum has been the industry's standard dummy text ever since the 1500s</p>
<div class="abs hero-btn">GET A FREE ESTIMATE</div>

<!-- About -->
<div class="abs about-band"></div>
<div class="abs label" style="left:163px;top:752px;color:var(--navy)">About Us</div>
<h2 class="abs title" style="left:163px;top:768px;color:var(--white)">Welcome To Palisade Lift<br>Inc</h2>
<div class="abs underline" style="left:163px;top:846px;background:var(--white)"></div>
<div class="abs about-img" role="img" aria-label="Elevator lobby with stainless steel doors, dark stone walls and potted plants"></div>
<div class="abs about-card">
  <p class="body-text">Lorem Ipsum is simply dummy text of the printing and typesetting industry. Lorem Ipsum has been the industry's standard dummy text ever since the 1500s, when an unknown printer took a galley of type and scrambled it to make a type specimen book. It has survived not only five centuries, but also the leap into electronic typesetting, remaining essentially unchanged. It was popularised in the 1960s with the release of Letraset sheets containing Lorem Ipsum passages.</p>
  <div class="more" style="margin-top:30px">READ MORE <svg viewBox="0 0 16 10"><path d="M0 5h14M10 1l4 4-4 4" stroke="currentColor" fill="none" stroke-width="1.4"/></svg></div>
</div>

<!-- Gallery & services -->
<div class="abs dark"></div>
<div class="abs label" style="left:163px;top:1513px">Gallery</div>
<h2 class="abs title" style="left:163px;top:1530px;color:var(--white)">Our Latest Projects</h2>
<div class="abs underline" style="left:163px;top:1568px"></div>
<div class="abs gallery-img" style="left:161px;background:linear-gradient(135deg,#d6dadf,#8e959d)" role="img" aria-label="Modern grey stone elevator lobby"></div>
<div class="abs col-rule" style="left:440px"></div>
<div class="abs gallery-img" style="left:480px;background:linear-gradient(135deg,#c9b89e,#7a8590)" role="img" aria-label="Glass panoramic elevator car in an atrium"></div>
<div class="abs col-rule" style="left:759px"></div>
<div class="abs gallery-img" style="left:798px;background:linear-gradient(135deg,#eef0f0,#a8c7b9)" role="img" aria-label="Home elevator cabin beside a pale green wall"></div>

<div class="abs label" style="left:0;top:2020px;width:1200px;text-align:center">Services</div>
<h2 class="abs title" style="left:0;top:2035px;width:1200px;text-align:center;color:var(--white)">What We Provide</h2>
<div class="abs underline" style="left:558px;top:2074px"></div>

<div class="abs services">
  <div class="service">
    <svg class="icon" viewBox="0 0 44 44" fill="none" stroke="#10a4f9" stroke-width="1.5"><rect x="12" y="14" width="20" height="16"/><circle cx="22" cy="22" r="4"/><path d="M4 22h8M32 22h8M22 4v10M22 30v10"/></svg>
    <h3>MODERNIZATION</h3><div class="bar"></div>
    <p>Lorem Ipsum is simply dummy text of the printing and typesetting industry. Lorem Ipsum has been the industry's standard dummy text.</p>
    <div class="more">READ MORE <svg viewBox="0 0 16 10"><path d="M0 5h14M10 1l4 4-4 4" stroke="currentColor" fill="none" stroke-width="1.4"/></svg></div>
  </div>
  <div class="service">
    <svg class="icon" viewBox="0 0 44 44" fill="none" stroke="#10a4f9" stroke-width="1.5"><circle cx="16" cy="16" r="8"/><circle cx="16" cy="16" r="3"/><circle cx="29" cy="29" r="9"/><circle cx="29" cy="29" r="3.5"/></svg>
    <h3>MAINTENANCE</h3><div class="bar"></div>
    <p>Lorem Ipsum is simply dummy text of the printing and typesetting industry. Lorem Ipsum has been the industry's standard dummy text.</p>
    <div class="more">READ MORE <svg viewBox="0 0 16 10"><path d="M0 5h14M10 1l4 4-4 4" stroke="currentColor" fill="none" stroke-width="1.4"/></svg></div>
  </div>
  <div class="service active">
    <svg class="icon" viewBox="0 0 44 44" fill="none" stroke="#ffffff" stroke-width="1.5"><rect x="26" y="6" width="12" height="34"/><circle cx="14" cy="8" r="3"/><path d="M14 12v14l-4 14M14 26l4 14M14 16l10-4"/></svg>
    <h3>SERVICE &amp; REPAIR</h3><div class="bar"></div>
    <p>Lorem Ipsum is simply dummy text of the printing and typesetting industry. Lorem Ipsum has been the industry's standard dummy text.</p>
    <div class="more">READ MORE <svg viewBox="0 0 16 10"><path d="M0 5h14M10 1l4 4-4 4" stroke="currentColor" fill="none" stroke-width="1.4"/></svg></div>
  </div>
  <div class="service">
    <svg class="icon" viewBox="0 0 44 44" fill="none" stroke="#10a4f9" stroke-width="1.5"><rect x="4" y="4" width="36" height="36"/><rect x="10" y="12" width="10" height="28"/><rect x="24" y="12" width="10" height="28"/></svg>
    <h3>RAIL INSTALLATION...</h3><div class="bar"></div>
    <p>Lorem Ipsum is simply dummy text of the printing and typesetting industry. Lorem Ipsum has been the industry's standard dummy text.</p>
    <div class="more">READ MORE <svg viewBox="0 0 16 10"><path d="M0 5h14M10 1l4 4-4 4" stroke="currentColor" fill="none" stroke-width="1.4"/></svg></div>
  </div>
</div>

<!-- Video -->
<div class="abs video" role="img" aria-label="Looking up between two glass skyscrapers into a cloudy sky"></div>
<div class="abs play"><svg width="16" height="16" viewBox="0 0 16 16"><path d="M5 3l8 5-8 5z" fill="#fff"/></svg></div>

<!-- FAQ -->
<div class="abs faq-img" role="img" aria-label="Business people riding a glass elevator with warm lights"></div>
<div class="abs label" style="left:612px;top:2988px">Faq's</div>
<h2 class="abs title" style="left:612px;top:3003px">Question &amp; Answer</h2>
<div class="abs underline" style="left:612px;top:3043px"></div>
<div class="abs faq-card">
  <h4><span>Q.1</span> Lorem Ipsum is simply dummy text of the printing and typesetting industry ?</h4>
  <p class="body-text">Lorem Ipsum is simply dummy text of the printing and typesetting industry. Lorem Ipsum has been the industry's standard dummy text ever since the 1500s, when an unknown printer took a galley of type and scrambled it to make a type specimen book. It has survived not only five centuries, but also the leap into electronic typesetting.</p>
  <div class="more" style="margin-top:20px">READ MORE <svg viewBox="0 0 16 10"><path d="M0 5h14M10 1l4 4-4 4" stroke="currentColor" fill="none" stroke-width="1.4"/></svg></div>
</div>
<div class="abs dots"><i></i><i class="on"></i><i></i><i></i><i></i></div>

<!-- Contact -->
<div class="abs contact"></div>
<div class="abs label" style="left:0;top:3471px;width:1200px;text-align:center">Get In Touch</div>
<h2 class="abs title" style="left:0;top:3486px;width:1200px;text-align:center">Contact Us</h2>
<div class="abs underline" style="left:558px;top:3525px"></div>
<p class="abs body-text" style="left:340px;top:3542px;width:520px;text-align:center">Lorem Ipsum is simply dummy text of the printing and typesetting industry. Lorem Ipsum has been the industry's standard dummy text ever since the 1500s, when an unknown printer took a galley of type and scrambled it to make a type specimen book. It has survived not only five centuries.</p>

<div class="abs contact-info">
  <div class="info-item">
    <div class="h"><svg viewBox="0 0 18 18"><path d="M4 1l3 4-2 2c1 2 3 4 5 5l2-2 4 3-2 3C8 16 2 10 1 4z" fill="#0b1f3f"/></svg>CALL US</div>
    <p>(555) 010 4827</p>
  </div>
  <div class="info-item">
    <div class="h"><svg viewBox="0 0 18 18"><rect x="1" y="4" width="16" height="11" fill="#0b1f3f"/><path d="M1 4l8 6 8-6" stroke="#fff" fill="none"/></svg>MAIL US</div>
    <p>hello@palisadelift.ca</p>
  </div>
  <div class="info-item">
    <div class="h"><svg viewBox="0 0 18 18"><path d="M9 1a5 5 0 0 1 5 5c0 4-5 9-5 9S4 10 4 6a5 5 0 0 1 5-5z" fill="#0b1f3f"/><circle cx="9" cy="6" r="2" fill="#fff"/></svg>ADDRESS</div>
    <p>100 lorem ipsum is simply dummy text.</p>
  </div>
</div>
<div class="abs contact-btn">GET A FREE QUOTE</div>

<div class="abs contact-form">
  <div class="field">Name*</div>
  <div class="field">Phone*</div>
  <div class="field">Email*</div>
  <div class="field msg">Message*</div>
  <div class="send">DROP A MESSAGE</div>
</div>

<!-- Footer -->
<div class="abs footer" role="img" aria-label="Dark blue tinted photo of city office towers"></div>
<div class="abs brand" style="left:0;top:4205px;width:1200px;text-align:center">PALISADE LIFT INC</div>
<nav class="abs foot-nav"><span>Home</span><span>About Us</span><span>Services</span><span>Gallery</span><span>Faq</span><span>Contact Us</span></nav>
<div class="abs foot-rule"></div>
<div class="abs follow">FOLLOW US ON</div>
<div class="abs social"><i></i><i class="on"></i><i></i><i></i></div>
<div class="abs copy">Copyright © 2020 <span>Palisade Lift Inc.</span> All Rights Resereved. Terms &amp; Conditions</div>

</body>
</html>
```